LLC needs a business card design that emphasizes consulting and expert witness in upstream oil and g

I need a business card design for my company called Kelvora Consultative Service, LLC. My expertise is in oil and gas upstream operations management to optimize performance and also as an expert witness for law firms in oil and gas upstream operations litigation.
The final design should communicate knowledge and hands-on experience as well as trust. (Kelvora means rope or lasso. Perhaps "Kelvora" should be in the form of a rope.) I do not like the color green in any shade. My first preference would be some shade of blue.
Oil And Gas

```html
<!DOCTYPE html>
<html lang="en">
<head>
<meta charset="utf-8">
<title>Kelvora Consultative Service – Business Card</title>
<link href="https://fonts.googleapis.com/css2?family=Mulish:wght@300;400;600;700;800&display=swap" rel="stylesheet">
<style>
  :root {
    --page-bg: #ffffff;
    --navy: #2d4a9d;
    --navy-deep: #2b3f8f;
    --sky: #0fb6ec;
    --sky-light: #8fdcf6;
    --sky-pale: #e8f8fe;
    --disc-dark: #1565b6;
    --white: #ffffff;
    --text-light: #dfe6f7;
  }
  * { box-sizing: border-box; margin: 0; padding: 0; }
  html, body {
    width: 1200px; height: 1000px; overflow: hidden;
    background: var(--page-bg);
    font-family: "Mulish", sans-serif;
  }
  .canvas {
    position: relative; width: 1200px; height: 1000px;
  }
  .card {
    position: absolute; top: 349px;
    width: 530px; height: 302px;
    overflow: hidden;
    box-shadow: 0 22px 40px rgba(0,0,0,0.22), 0 4px 10px rgba(0,0,0,0.12);
  }
  /* Front */
  .card--front { left: 50px; background: var(--white); }
  .front-band {
    position: absolute; left: 0; right: 0; bottom: 0; height: 102px;
    background: linear-gradient(to bottom, var(--white) 0%, var(--sky-pale) 25%, var(--sky-light) 70%, var(--sky) 100%);
  }
  .brand {
    position: absolute; left: 88px; top: 72px;
    display: flex; align-items: center; gap: 16px;
  }
  .brand-disc {
    width: 104px; height: 104px; border-radius: 50%;
    background: var(--sky); flex: none;
  }
  .brand-name {
    font-size: 56px; font-weight: 800; color: var(--navy);
    line-height: 1; letter-spacing: -0.5px;
  }
  .brand-sub {
    font-size: 16px; font-weight: 400; color: var(--sky);
    margin-top: 6px; letter-spacing: 0.1px;
  }
  .tagline {
    position: absolute; left: 0; right: 0; top: 254px;
    text-align: center; font-size: 15px; font-weight: 400;
    color: var(--navy-deep); letter-spacing: -0.2px;
  }
  /* Back */
  .card--back { left: 620px; background: var(--navy); }
  .back-disc { position: absolute; left: 0; top: 0; }
  .contact {
    position: absolute; right: 48px; top: 92px; text-align: right;
    color: var(--white);
  }
  .person-name { font-size: 18px; font-weight: 700; line-height: 1.1; }
  .person-role { font-size: 17px; font-weight: 300; color: var(--text-light); line-height: 1.1; }
  .company { margin-top: 42px; font-size: 17px; font-weight: 600; color: var(--sky); }
  .details { margin-top: 3px; font-size: 14px; font-weight: 400; line-height: 19px; color: var(--text-light); }
</style>
</head>
<body>
<main class="canvas">
  <section class="card card--front" aria-label="Business card front">
    <div class="front-band"></div>
    <div class="brand">
      <div class="brand-disc"></div>
      <div class="brand-text">
        <div class="brand-name">Kelvora</div>
        <div class="brand-sub">Kelvora Consultative Service, LLC</div>
      </div>
    </div>
    <p class="tagline">oil and gas upstream operations management &nbsp;&amp; expert witness services</p>
  </section>

  <section class="card card--back" aria-label="Business card back">
    <svg class="back-disc" width="200" height="302" viewBox="0 0 200 302" aria-hidden="true">
      <circle cx="57" cy="149" r="110" fill="var(--disc-dark)"/>
    </svg>
    <div class="contact">
      <div class="person-name">John Doe</div>
      <div class="person-role">Director</div>
      <div class="company">Kelvora Consultative Service, LLC</div>
      <div class="details">
        123 Any Street<br>
        Any Town<br>
        Telephone 1234 5678<br>
        www.kelvora.com
      </div>
    </div>
  </section>
</main>
</body>
</html>
```